Virgin Coconut Oil Label

Need to update label to a newer design using all the same information. Our company manufactures Coconut Products.
Target Market(s)
Pharmacies, dept stores, groceries.
Look and feel
Each slider illustrates characteristics of the customer's brand and the style your logo design should communicate.

```html
<!DOCTYPE html>
<html lang="en">
<head>
<meta charset="utf-8">
<title>Palmara Extra Virgin Coconut Oil – Label</title>
<link rel="stylesheet" href="https://fonts.googleapis.com/css2?family=Crimson+Text:ital,wght@0,400;0,600;0,700;1,400&display=swap">
<style>
  :root {
    --page: #ededed;
    --label: #ffffff;
    --green: #5f9e6e;
    --green-dark: #3f7a4f;
    --ink: #4a4a4a;
    --ink-soft: #7a7a7a;
    --coconut-brown: #8a6a50;
    --coconut-flesh: #f3efe6;
  }
  * { box-sizing: border-box; margin: 0; padding: 0; }
  html, body { width: 720px; height: 1200px; overflow: hidden; }
  body {
    background: var(--page);
    font-family: "Crimson Text", "Times New Roman", serif;
    color: var(--ink);
    display: flex;
    gap: 40px;
    justify-content: center;
    align-items: center;
  }
  .label {
    width: 300px;
    height: 840px;
    background: var(--label);
    position: relative;
    display: flex;
    flex-direction: column;
    align-items: center;
    box-shadow: 0 2px 10px rgba(0,0,0,0.08);
  }
  .cap-band {
    width: 100%;
    height: 18px;
    background: var(--green);
  }
  /* Front */
  .claim {
    margin-top: 150px;
    text-align: center;
    font-weight: 700;
    font-size: 13px;
    letter-spacing: 0.5px;
    line-height: 1.25;
    color: var(--ink);
  }
  .brand-band {
    margin-top: 14px;
    width: 100%;
    height: 58px;
    background: var(--green);
    display: flex;
    align-items: center;
    justify-content: center;
    gap: 10px;
  }
  .brand-mark {
    width: 14px; height: 14px; border-radius: 50%;
    background: var(--label);
  }
  .brand-name {
    font-weight: 600;
    font-size: 26px;
    letter-spacing: 2px;
    color: var(--label);
  }
  .product-kind {
    margin-top: 18px;
    font-size: 17px;
    letter-spacing: 1px;
    color: var(--ink-soft);
  }
  .product-name {
    font-size: 36px;
    font-weight: 400;
    letter-spacing: 1px;
    line-height: 1;
    color: var(--ink);
  }
  .product-traits {
    margin-top: 8px;
    font-size: 15px;
    color: var(--ink-soft);
  }
  .coconut-art {
    margin-top: 26px;
    width: 230px;
    height: 220px;
    background: radial-gradient(ellipse at 50% 55%,
      var(--coconut-flesh) 0%,
      #e9dfd2 35%,
      rgba(138,106,80,0.35) 58%,
      rgba(255,255,255,0) 72%);
  }
  .front-footer {
    position: absolute;
    bottom: 110px;
    font-size: 10px;
    letter-spacing: 1.5px;
    text-transform: uppercase;
    color: var(--green-dark);
  }
  /* Back */
  .back-band {
    margin-top: 202px;
    width: 100%;
    height: 22px;
    background: var(--green);
  }
  .back-copy {
    width: 100%;
    padding: 20px 28px 0;
  }
  .back-heading {
    font-size: 22px;
    font-weight: 400;
    color: var(--ink);
    margin-top: 14px;
  }
  .back-heading:first-child { margin-top: 0; }
  .back-text {
    font-size: 11px;
    line-height: 1.35;
    color: var(--ink-soft);
    margin-top: 4px;
  }
  .back-text.notice { font-weight: 600; color: var(--ink); margin-top: 6px; }
  .manufacturer {
    position: absolute;
    bottom: 110px;
    text-align: center;
    font-size: 10px;
    line-height: 1.35;
    color: var(--ink-soft);
  }
  .manufacturer strong { font-weight: 600; color: var(--ink); }
</style>
</head>
<body>

  <section class="label label-front">
    <div class="cap-band"></div>
    <p class="claim">100% PURE ORGANIC<br>PRODUCT OF PHILIPPINES</p>
    <div class="brand-band">
      <span class="brand-mark"></span>
      <span class="brand-name">Palmara</span>
    </div>
    <p class="product-kind">EXTRA VIRGIN</p>
    <h1 class="product-name">COCONUT OIL</h1>
    <p class="product-traits">Natural · Unrefined · Cold · Pressed</p>
    <div class="coconut-art" role="img" aria-label="Illustration of a halved coconut with coconut oil pouring from it"></div>
    <p class="front-footer">No additives and preservatives added.</p>
  </section>

  <section class="label label-back">
    <div class="cap-band"></div>
    <div class="back-band"></div>
    <div class="back-copy">
      <h2 class="back-heading">Ingredients:</h2>
      <p class="back-text">100% Pure Organic Extra Virgin Coconut Oil</p>

      <h2 class="back-heading">Recommended usage:</h2>
      <p class="back-text">Take 1–3 tablespoons daily as a supplement. Can be taken orally or mixed with food. Ideal as an ingredient for salad dressings.</p>
      <p class="back-text notice">Do not use if seal is broken.</p>

      <h2 class="back-heading">Storage condition:</h2>
      <p class="back-text">Store at room temperature below 25°C. Keep tightly closed after every use. Avoid direct sunlight. Do not refrigerate.</p>
    </div>
    <p class="manufacturer">
      Manufactured by:<br>
      <strong>COASTLINE HARVEST FOODS, INC.</strong><br>
      Lot 7 Bayside Road, Seaview City<br>
      (042) 555 0186
    </p>
  </section>

</body>
</html>
```